CONDOMS Packaging Design Project

we are in need of the following:
1)a colorfull display box of 36 sales pack of 2 condoms with size when folded:
W=190mm,H=80mm,D=130mm
2)sales pack of 2 retangular foil condoms with sizes when folded:
Cover-W=60mm,H=62mm,D=12mm
drawer-W=59mm,H=61mm,D=11mm
The brand is VOLK,the UPC is WARM TIDE CONDOMS because it is benzocaine based to prolong the erection.
The sales pack packaging should be innovative,attractive,easy to open in the darkness,slim, thin,flat,12mm maximum as thickness for discretion,easy to be inserted into the pocket.

Our company logo,email,and other will be uploaded at final.
Only high qualified designers are welcome on this project.
Updates

Target Market(s)

15 to 35 years old men.

Industry/Entity Type

It Company

Requirements
Must have
• the sales pack of 2 condoms should be slim,thin,flat with 12mm of thickness for discretion but with hanger part to have the product visible at the reatail stores so if you can mix the 7x7 pack packaging with halvex packaging that will be great.the both packagings are in the attached files.
The design should have:
1)Map printing sales pack and display box.
2)map cutting sales pack and display box.
Nice to have
• The sales pack packaging should be innovative,attractive,easy to open in the darkness,slim and thin for discretion,easy to be inserted into the pocket,incisive colors to attract people.It will have 2 rectangular condoms foil inside.

The brand VOLK should be noted impressively like a merrovan and Castelvardo cars are for the public to penetrate the mind of the consumers as premium quality and assurance.
Should not have
• 1)avoid large size sales pack packaging.
2)avoid to exceed 12mm as thickness of the sales pack.

```html
<!DOCTYPE html>
<html lang="en">
<head>
<meta charset="utf-8">
<title>VOLK Sales Pack – Dieline Schematic</title>
<link href="https://fonts.googleapis.com/css2?family=Marcellus&family=Montserrat:wght@400;500&family=Jost:wght@300;400;500&display=swap" rel="stylesheet">
<style>
  :root {
    --paper: #ffffff;
    --navy: #1b2a3b;
    --navy-deep: #142131;
    --foil-light: #3a4a5e;
    --black: #050505;
    --charcoal: #2a2a2a;
    --silver: #c9ccd1;
    --muted: #8a94a2;
    --rule: #6f8197;
    --outline: #cfd3d8;
    --label-ink: #222222;
  }
  * { margin: 0; padding: 0; box-sizing: border-box; }
  html, body { width: 1200px; height: 927px; overflow: hidden; background: var(--paper); }
  .sheet { position: relative; width: 1200px; height: 927px; background: var(--paper); font-family: "Jost", sans-serif; }

  .schematic-label {
    position: absolute; left: 85px; top: 135px; width: 194px; height: 44px;
    border: 1px solid #bfbfbf; display: flex; align-items: center; justify-content: center;
    font-family: "Jost", sans-serif; font-size: 11px; letter-spacing: .2px; color: var(--label-ink);
  }

  .panel { position: absolute; overflow: hidden; }

  /* brand lockup */
  .wordmark {
    position: absolute; left: 0; right: 0; text-align: center;
    font-family: "Marcellus", serif; color: var(--silver); letter-spacing: 5px; line-height: 1;
  }
  .tagline {
    position: absolute; left: 0; right: 0; text-align: center;
    font-family: "Montserrat", sans-serif; color: var(--silver); letter-spacing: 1.6px; line-height: 1;
  }
  .count-line {
    font-family: "Marcellus", serif; font-size: 5.5px; letter-spacing: .5px; color: var(--silver); text-align: center;
  }
  .count-line b { font-size: 7px; font-weight: 400; }

  /* foil wrapper */
  .foil {
    left: 152px; top: 519px; width: 139px; height: 138px;
    background: radial-gradient(circle at 50% 45%, var(--foil-light) 0%, var(--navy) 60%, var(--navy-deep) 100%);
  }
  .foil-edge {
    position: absolute; inset: 0;
    background:
      linear-gradient(90deg, #2d3d52 0 9px, transparent 9px calc(100% - 9px), #2d3d52 calc(100% - 9px)),
      linear-gradient(180deg, #2d3d52 0 9px, transparent 9px calc(100% - 9px), #2d3d52 calc(100% - 9px));
    opacity: .8;
  }
  .foil .wordmark { top: 56px; font-size: 30px; color: #7b8797; }
  .foil .tagline { top: 82px; font-size: 6.5px; color: #7b8797; }

  /* open sleeve with foil inside */
  .sleeve-open { left: 317px; top: 345px; width: 149px; height: 312px; background: var(--navy); }
  .notch-top {
    position: absolute; top: 0; left: 54px; width: 42px; height: 19px;
    background: var(--paper); border-radius: 0 0 9px 9px;
  }
  .notch-bottom {
    position: absolute; bottom: 0; width: 42px; height: 18px;
    background: var(--paper); border-radius: 9px 9px 0 0;
  }
  .caution {
    position: absolute; top: 60px; left: 14px; right: 14px; text-align: center;
    font-size: 5.6px; line-height: 1.35; color: var(--muted); font-weight: 300;
  }
  .caution p + p { margin-top: 7px; }
  .fold-rule { position: absolute; left: 0; right: 0; height: 1px; background: var(--rule); opacity: .7; }
  .sleeve-open .inner-foil {
    position: absolute; left: 7px; top: 173px; width: 135px; height: 112px;
    background: radial-gradient(circle at 50% 55%, var(--foil-light) 0%, var(--navy) 65%, var(--navy-deep) 100%);
  }
  .sleeve-open .inner-foil .wordmark { top: 58px; font-size: 30px; color: #7b8797; }
  .sleeve-open .inner-foil .tagline { top: 83px; font-size: 6.5px; color: #7b8797; }
  .drawer-band {
    position: absolute; left: 0; right: 0; bottom: 0; height: 29px;
    background: linear-gradient(180deg, #1a1a1a, var(--black));
  }
  .drawer-band .count-line { margin-top: 5px; }
  .pull-tab { position: absolute; left: 50%; transform: translateX(-50%); width: 28px; height: 3px; border: 1px solid #777; border-radius: 2px; }
  .drawer-band .pull-tab { top: 17px; }
  .drawer-hint { position: absolute; left: 376px; top: 672px; width: 31px; height: 2px; background: #333; }

  /* printed outer sleeve */
  .sleeve-print {
    left: 491px; top: 315px; width: 148px; height: 342px;
    background: linear-gradient(90deg, #2a2a2a 0%, var(--black) 12%, var(--black) 88%, #2a2a2a 100%);
  }
  .sleeve-print .top-band { position: absolute; top: 0; left: 0; right: 0; height: 30px; }
  .sleeve-print .top-band .count-line { margin-top: 5px; }
  .sleeve-print .top-band .pull-tab { top: 20px; }
  .iso-mark {
    position: absolute; top: 50px; right: 15px; font-size: 6px; color: var(--silver);
    transform: rotate(180deg); letter-spacing: .3px;
  }
  .spine { position: absolute; left: 0; right: 0; top: 176px; height: 18px; background: var(--charcoal); }
  .distributor {
    position: absolute; display: flex; align-items: center; gap: 3px;
    font-family: "Jost", sans-serif; font-size: 5.5px; font-weight: 500; letter-spacing: .4px; color: var(--silver);
  }
  .distributor .dot { width: 7px; height: 7px; border-radius: 50%; background: var(--silver); }
  .sleeve-print .distributor { top: 209px; left: 14px; }
  .sleeve-print .wordmark { top: 244px; font-size: 31px; }
  .sleeve-print .tagline { top: 272px; font-size: 7px; }
  .slogan { position: absolute; bottom: 13px; font-family: "Montserrat", sans-serif; font-size: 6.5px; font-weight: 500; color: #e6e6e6; }
  .slogan.left { left: 14px; }
  .slogan.right { right: 11px; }

  /* inner side of sleeve */
  .sleeve-inside { left: 665px; top: 315px; width: 148px; height: 342px; background: var(--navy); }
  .sleeve-inside .fold-rule { background: #8fa0b3; }

  /* assembled pack with hanger */
  .hanger-tab { position: absolute; left: 895px; top: 473px; width: 38px; height: 40px; }
  .hanger-flat { position: absolute; left: 1011px; top: 471px; width: 38px; height: 57px; }
  .pack {
    left: 839px; top: 512px; width: 149px; height: 145px;
    background: linear-gradient(90deg, #2a2a2a 0%, var(--black) 12%, var(--black) 88%, #2a2a2a 100%);
  }
  .pack .distributor { top: 13px; left: 14px; }
  .pack .wordmark { top: 50px; font-size: 31px; }
  .pack .tagline { top: 78px; font-size: 7px; }
  .pack .drawer-band { height: 30px; background: linear-gradient(180deg, #1e1e1e, #0c0c0c); }
  .pack .drawer-band .count-line { margin-top: 6px; }
  .pack .drawer-band .pull-tab { top: 18px; }
</style>
</head>
<body>
<div class="sheet">

  <div class="schematic-label">FOR SCHEMATIC USE ONLY</div>

  <!-- single foil -->
  <div class="panel foil" role="img" aria-label="Condom foil wrapper with fine radiating line pattern along the edges">
    <div class="foil-edge"></div>
    <div class="wordmark">VOLK</div>
    <div class="tagline">WARM TIDE CONDOMS</div>
  </div>

  <!-- open sleeve showing foil and drawer -->
  <div class="panel sleeve-open">
    <div class="notch-top"></div>
    <div class="caution">
      <p>Caution: This Product Contains Natural Rubber Latex Which May Cause Allergic Reaction</p>
      <p>Latex condoms are intended to prevent pregnancy, HIV/AIDS, and other STD's.</p>
    </div>
    <div class="fold-rule" style="top:164px"></div>
    <div class="inner-foil" role="img" aria-label="Condom foil wrapper seen through open sleeve">
      <div class="wordmark">VOLK</div>
      <div class="tagline">WARM TIDE CONDOMS</div>
    </div>
    <div class="drawer-band">
      <div class="count-line"><b>2</b> PREMIUM LATEX CONDOMS</div>
      <div class="pull-tab"></div>
    </div>
  </div>
  <div class="drawer-hint"></div>

  <!-- printed outer sleeve -->
  <div class="panel sleeve-print">
    <div class="top-band">
      <div class="count-line"><b>2</b> PREMIUM LATEX CONDOMS</div>
      <div class="pull-tab"></div>
    </div>
    <div class="iso-mark">ISO 4074:2002</div>
    <div class="spine"></div>
    <div class="distributor"><span class="dot"></span>HERONVALE</div>
    <div class="wordmark">VOLK</div>
    <div class="tagline">WARM TIDE CONDOMS</div>
    <div class="slogan left">GET IT ON.</div>
    <div class="slogan right">KEEP IT ON.</div>
    <div class="notch-bottom" style="left:53px"></div>
  </div>

  <!-- inner face of sleeve -->
  <div class="panel sleeve-inside">
    <div class="fold-rule" style="top:27px"></div>
    <div class="fold-rule" style="top:176px"></div>
    <div class="fold-rule" style="top:194px"></div>
    <div class="notch-bottom" style="left:53px"></div>
  </div>

  <!-- hanger tabs -->
  <svg class="hanger-tab" viewBox="0 0 38 40">
    <path d="M1 40 V19 A18 18 0 0 1 37 19 V40" fill="#fff" stroke="var(--outline)" stroke-width="1"/>
    <circle cx="19" cy="20" r="6" fill="none" stroke="var(--outline)" stroke-width="1"/>
  </svg>
  <svg class="hanger-flat" viewBox="0 0 38 57">
    <path d="M1 19 A18 18 0 0 1 37 19 V46 A10 10 0 0 1 27 56 H11 A10 10 0 0 1 1 46 Z" fill="#fff" stroke="var(--outline)" stroke-width="1"/>
    <circle cx="19" cy="20" r="6" fill="none" stroke="var(--outline)" stroke-width="1"/>
    <line x1="2" y1="37" x2="36" y2="37" stroke="var(--outline)" stroke-width="1" stroke-dasharray="3 2"/>
  </svg>

  <!-- assembled pack -->
  <div class="panel pack">
    <div class="distributor"><span class="dot"></span>HERONVALE</div>
    <div class="wordmark">VOLK</div>
    <div class="tagline">WARM TIDE CONDOMS</div>
    <div class="drawer-band">
      <div class="count-line"><b>2</b> PREMIUM LATEX CONDOMS</div>
      <div class="pull-tab"></div>
    </div>
  </div>

</div>
</body>
</html>
```